Velmo (Pathways for company scale) website

My plan is to offer a marketplace where by businesses (SME and Corporates) are able to post specific requirements, be that debt funding advice or other types of advice (legal/accountant) on the velmo website and advisors can seek to 'pitch' to the client.

clients should be anonymous - maybe a specific client number? (this is reduces the risk of bypass) and have the ability to choose the advisor via the advisors profile.

Advisors could potential use there Netlyne profile to auto complete on Velmo - not sure if this is possible or costs involved, however this would be ideal.

I would think Wordpress would be the best platform for this type of platform, however I would be guided by the experts.

I would need any code written in html 5 to allow for various devices (mobile, tablets, desktop)

Logo design is currently being completed also via Sketch Hive and I'm finalising colours ext now, so could provide advice in due course.

additional requirements (medium to longer term)
longer term I would be looking to add addition aspects to the site including algorithms, specific financial calculations, some of which I would be able to complete myself.

similar websites would be:
https://www.taskquill.example.au
http://www.fundoraxi.example.au

Industry/Entity Type

Debt

Coding

Coded - Design and coding required

```html
<!DOCTYPE html>
<html lang="en">
<head>
<meta charset="utf-8">
<title>Velmo – Pathways for company scale</title>
<link href="https://fonts.googleapis.com/css2?family=Open+Sans:ital,wght@0,300;0,400;0,600;0,700;1,400&display=swap" rel="stylesheet">
<style>
:root{
  --green:#1f9e55;
  --green-light:#7fe0a6;
  --blue:#4a63b5;
  --blue-deep:#2b4c9f;
  --cyan:#3fb5e5;
  --ink:#333;
  --grey:#8a8a8a;
  --line:#dcdcdc;
  --band:#f1f1f1;
  --dark:#262626;
}
*{box-sizing:border-box;margin:0;padding:0}
html,body{width:1200px;height:3163px;overflow:hidden}
body{font-family:'Open Sans',Arial,sans-serif;color:var(--ink);background:#fff;position:relative}
section,header,footer{position:absolute;left:0;width:1200px}

/* header */
.site-header{top:0;height:101px;background:#fff}
.brand{position:absolute;left:101px;top:22px;font-size:50px;font-weight:300;color:var(--green);letter-spacing:1px;line-height:1}
.main-nav{position:absolute;left:430px;top:36px;display:flex;align-items:center;gap:0}
.main-nav a{font-size:15px;color:#666;text-decoration:none;margin-right:31px;line-height:38px}
.main-nav a.active{color:var(--green);font-weight:600}
.main-nav .btn-register{background:var(--blue);color:#fff;padding:0 20px;border-radius:3px;font-size:14px;margin:0 0 0 6px;height:38px}

/* hero */
.hero{top:101px;height:490px;background:linear-gradient(180deg,#e4e6e8 0%,#d3d6d9 55%,#b9bcc0 100%)}
.hero-box{position:absolute;left:101px;top:131px;width:422px;height:223px;background:rgba(255,255,255,.82);padding:14px 16px}
.hero-box h1{font-size:33px;font-weight:600;color:var(--blue);line-height:38px}
.hero-box p{font-size:14.5px;color:#555;line-height:23px;margin-top:10px}
.btn-more{display:inline-block;margin-top:16px;background:var(--blue);color:#fff;font-size:14px;font-weight:600;padding:8px 16px;border-radius:3px}
.slide-arrow{position:absolute;top:225px;width:32px;height:42px;background:rgba(120,120,120,.6);display:flex;align-items:center;justify-content:center}
.slide-arrow.prev{left:0}.slide-arrow.next{right:0}

/* services */
.services{top:591px;height:421px;text-align:center}
.section-title{font-size:29px;font-weight:600;color:#9a9a9a;position:absolute;top:68px;width:100%}
.service{position:absolute;top:137px;width:320px;text-align:center}
.service .ring{width:112px;height:112px;border:2px solid var(--green);border-radius:50%;margin:0 auto;display:flex;align-items:center;justify-content:center}
.service h3{font-size:19px;font-weight:600;color:var(--green);margin-top:28px}
.service p{font-size:13.5px;color:var(--grey);line-height:21px;margin-top:6px}

/* press */
.press{top:1012px;height:116px;background:var(--band);display:flex;align-items:center;justify-content:center;gap:48px}
.press span{font-size:22px;font-weight:700;color:#5c5c5c}
.press .badge{display:inline-block;width:22px;height:22px;border-radius:50%;background:#8c8c8c;vertical-align:middle;margin-right:8px}

/* why */
.why{top:1128px;height:823px;text-align:center}
.why h2{position:absolute;top:68px;width:100%;font-size:31px;font-weight:600;color:var(--blue)}
.why .lead{position:absolute;top:111px;width:100%;font-size:19px;color:#222}
.card{position:absolute;width:312px;height:281px;border:2px solid #e6e6e6;text-align:center;padding-top:40px}
.card .art{width:92px;height:78px;margin:0 auto;border-radius:10px}
.card h3{font-size:20px;font-weight:400;color:var(--blue);margin-top:22px}
.card p{font-size:13.5px;color:var(--grey);line-height:19px;margin:6px 26px 0}

/* testimonials */
.testimonials{top:1951px;height:455px;background:linear-gradient(180deg,#2c2c2c,#141414 60%,#0c0c0c)}
.testimonials h2{position:absolute;top:93px;width:100%;text-align:center;font-size:30px;font-weight:600;color:var(--green-light)}
.testimonials .lead{position:absolute;top:135px;width:100%;text-align:center;font-size:21px;color:#fff}
.avatar{position:absolute;left:127px;top:226px;width:126px;height:126px;border-radius:50%;background:linear-gradient(160deg,#d7d2cc,#a9a29a);border:5px solid #fff}
.quote{position:absolute;left:272px;top:235px;width:810px;font-size:13.5px;font-style:italic;color:#fff;line-height:25px}
.quote cite{display:block;font-style:normal;color:var(--green-light);margin-top:6px}
.t-arrow{position:absolute;top:160px;font-size:34px;color:#888;font-weight:300}

/* share */
.share{top:2406px;height:152px;display:flex;align-items:center;justify-content:center}
.share h4{font-size:24px;font-weight:600;color:#333;margin-right:20px}
.dots{display:flex;gap:8px}
.dots i{width:34px;height:34px;border-radius:50%;display:block}

/* newsletter */
.newsletter{top:2558px;height:180px;background:var(--blue-deep)}
.newsletter h2{position:absolute;left:243px;top:30px;font-size:34px;font-weight:600;color:#fff}
.newsletter h2 small{font-size:15px;font-weight:400;margin-left:6px}
.field{position:absolute;top:85px;height:48px;background:#fff;font-size:15px;color:#555;padding:13px 20px}
.btn-sub{position:absolute;left:827px;top:85px;width:130px;height:48px;background:var(--cyan);color:#fff;font-weight:600;font-size:16px;display:flex;align-items:center;justify-content:center}

/* links */
.links{top:2738px;height:263px;background:#f7f7f7}
.links .col{position:absolute;top:34px}
.links h5{font-size:17px;font-weight:600;color:var(--blue)}
.links ul{position:absolute;top:42px;list-style:none;width:200px}
.links li{font-size:13px;color:#666;line-height:27px}
.links li::before{content:"•";margin-right:7px;color:#999}
.links .rule{position:absolute;top:36px;width:1px;height:196px;background:var(--line)}

/* footer */
.site-footer{top:3001px;height:162px;background:var(--dark)}
.foot-nav{position:absolute;top:28px;width:100%;text-align:center}
.foot-nav a{font-size:13.5px;color:#ddd;text-decoration:none;margin:0 14px}
.foot-nav a::before{content:"•";margin-right:6px;color:#888}
.foot-rule{position:absolute;left:101px;right:101px;top:76px;height:1px;background:#444}
.copyright{position:absolute;left:101px;top:111px;font-size:13.5px;color:#bbb}
.foot-dots{position:absolute;left:937px;top:104px;display:flex;gap:10px}
.foot-dots i{width:33px;height:33px;border-radius:50%;display:block}
</style>
</head>
<body>

<header class="site-header">
  <div class="brand">velmo</div>
  <nav class="main-nav">
    <a class="active" href="#">Home</a><a href="#">About us</a><a href="#">Services</a><a href="#">Products</a><a href="#">Blog</a><a href="#">Login</a><a href="#">Help</a><a class="btn-register" href="#">REGISTER NOW</a>
  </nav>
</header>

<section class="hero" role="img" aria-label="Businessman in a suit leaning on a rooftop rail, looking at his phone above a hazy city skyline">
  <div class="hero-box">
    <h1>Phasellus rutrum magna vitae malesuada</h1>
    <p>Interdum et malesuada fames ac ante ipsum primis in faucibus. Morbi ultrices dolor nec ante pellentesque bibendum tempus pulvinar.</p>
    <span class="btn-more">READ MORE</span>
  </div>
  <div class="slide-arrow prev"><svg width="12" height="20"><path d="M10 2L2 10l8 8" stroke="#fff" stroke-width="2" fill="none"/></svg></div>
  <div class="slide-arrow next"><svg width="12" height="20"><path d="M2 2l8 8-8 8" stroke="#fff" stroke-width="2" fill="none"/></svg></div>
</section>

<section class="services">
  <div class="section-title">Curabitur consectetur risus eget</div>
  <div class="service" style="left:95px">
    <div class="ring"><svg width="34" height="24"><rect x="1" y="4" width="32" height="16" rx="2" fill="none" stroke="#1f9e55" stroke-width="2"/><line x1="6" y1="12" x2="28" y2="12" stroke="#1f9e55" stroke-width="2"/></svg></div>
    <h3>Proin consequat tortor</h3>
    <p>Fusce lobortis ante risus dictum condimentum vestibulum gravida urna. Integer vel neque elit. Pellentesque vitae sapien magna.</p>
  </div>
  <div class="service" style="left:441px">
    <div class="ring"><svg width="32" height="28"><path d="M2 2v24h28" stroke="#1f9e55" stroke-width="2.5" fill="none"/><path d="M7 19l7-7 5 5 9-10" stroke="#1f9e55" stroke-width="2.5" fill="none"/></svg></div>
    <h3>Cras commodoac</h3>
    <p>Fusce lobortis ante risus dictum condimentum vestibulum gravida urna. Integer vel neque elit. Pellentesque vitae sapien magna.</p>
  </div>
  <div class="service" style="left:785px">
    <div class="ring"><svg width="34" height="30"><circle cx="10" cy="9" r="5" fill="none" stroke="#1f9e55" stroke-width="2.5"/><path d="M2 28c0-7 4-11 8-11s8 4 8 11" stroke="#1f9e55" stroke-width="2.5" fill="none"/><rect x="22" y="16" width="4" height="12" fill="#1f9e55"/><rect x="28" y="11" width="4" height="17" fill="#1f9e55"/></svg></div>
    <h3>Nunc placerat arcu</h3>
    <p>Fusce lobortis ante risus dictum condimentum vestibulum gravida urna. Integer vel neque elit. Pellentesque vitae sapien magna.</p>
  </div>
</section>

<section class="press">
  <span>Morning Ledger</span>
  <span>Zentro</span>
  <span>cityherald</span>
  <span><i class="badge"></i>Brightwave</span>
  <span>Kestrel</span>
  <span>Startwire</span>
</section>

<section class="why">
  <h2>Why Choose Us?</h2>
  <p class="lead">Praesent elementum erat eget diam gravida</p>
  <div class="card" style="left:110px;top:159px"><div class="art" role="img" aria-label="Illustration of a desk lamp with coloured spheres" style="background:linear-gradient(135deg,#d8d8d8,#f3b24a 60%,#e44b3c)"></div><h3>Praesent velit nulla</h3><p>Condimentum vestibulum gravida urna. Integer vel neque elit. Pellentesque vitae sapien magna.</p></div>
  <div class="card" style="left:444px;top:159px"><div class="art" role="img" aria-label="Illustration of two chat speech bubbles" style="background:linear-gradient(135deg,#3d97d6,#8fd3f0)"></div><h3>Praesent velit nulla</h3><p>Condimentum vestibulum gravida urna. Integer vel neque elit. Pellentesque vitae sapien magna.</p></div>
  <div class="card" style="left:778px;top:159px"><div class="art" role="img" aria-label="Illustration of a megaphone" style="background:linear-gradient(135deg,#e9473c,#f5c23e)"></div><h3>Praesent velit nulla</h3><p>Condimentum vestibulum gravida urna. Integer vel neque elit. Pellentesque vitae sapien magna.</p></div>
  <div class="card" style="left:110px;top:460px"><div class="art" role="img" aria-label="Illustration of a profile card with a settings cog" style="background:linear-gradient(135deg,#2bb3b5,#9aa0a6 65%,#e4503f)"></div><h3>Praesent velit nulla</h3><p>Condimentum vestibulum gravida urna. Integer vel neque elit. Pellentesque vitae sapien magna.</p></div>
  <div class="card" style="left:444px;top:460px"><div class="art" role="img" aria-label="Illustration of an airmail envelope" style="background:linear-gradient(135deg,#e9e9e9,#c9d3e6)"></div><h3>Praesent velit nulla</h3><p>Condimentum vestibulum gravida urna. Integer vel neque elit. Pellentesque vitae sapien magna.</p></div>
  <div class="card" style="left:778px;top:460px"><div class="art" role="img" aria-label="Illustration of a red heart" style="background:linear-gradient(135deg,#f16a66,#e0413c)"></div><h3>Praesent velit nulla</h3><p>Condimentum vestibulum gravida urna. Integer vel neque elit. Pellentesque vitae sapien magna.</p></div>
</section>

<section class="testimonials" role="img" aria-label="Dark night photo of a suspension bridge over a city">
  <h2>Client’s Testimonials</h2>
  <p class="lead">Integer nulla quam, pellentesque sed tellus</p>
  <span class="t-arrow" style="left:42px">&#8249;</span>
  <span class="t-arrow" style="left:1136px">&#8250;</span>
  <div class="avatar" role="img" aria-label="Portrait of the client"></div>
  <blockquote class="quote">“ Nam a malesuada libero. Duis sodales et libero vel interdum. Interdum et malesuada fames ac ante ipsum primis in faucibus. Donec lobortis dui tortor, eu lobortis felis mattis nec. Sed justo quam, luctus eu mauris eget, euismod dapibus sem. Sed tempus feugiat ante, at ornare libero volutpat sed. Maecenas quis magna magna. ”
    <cite>Darren Oakley</cite>
  </blockquote>
</section>

<section class="share">
  <h4>Mauris gravida ligula nisi</h4>
  <div class="dots"><i style="background:#3b5a98"></i><i style="background:#2fa9e0"></i><i style="background:#333"></i><i style="background:#cb2027"></i><i style="background:#f57d00"></i><i style="background:#cd201f"></i><i style="background:#3f729b"></i><i style="background:#5aa13e"></i></div>
</section>

<section class="newsletter">
  <h2>GET UPDATED WITH US <small>Aenean eget turpis ut ligula fermentum imperdiet</small></h2>
  <div class="field" style="left:243px;width:276px">Name</div>
  <div class="field" style="left:536px;width:274px">E-Mail Address</div>
  <div class="btn-sub">SUBSCRIBE</div>
</section>

<section class="links">
  <div class="col" style="left:110px"><h5>Quick Links</h5>
    <ul style="left:10px"><li>Integer lobortis</li><li>Curabitur ac</li><li>Phasellus tellus nisl</li><li>Aenean fringilla</li><li>Vestibulum</li><li>Aliquam commodo</li></ul>
    <ul style="left:210px"><li>Integer lobortis</li><li>Curabitur ac</li><li>Phasellus tellus nisl</li><li>Aenean fringilla</li><li>Vestibulum</li><li>Aliquam commodo</li></ul>
  </div>
  <div class="rule" style="left:485px"></div>
  <div class="col" style="left:540px"><h5>Quick Links</h5>
    <ul style="left:8px"><li>Integer lobortis</li><li>Curabitur ac</li><li>Phasellus tellus nisl</li><li>Aenean fringilla</li><li>Vestibulum</li><li>Aliquam commodo</li></ul>
    <ul style="left:205px"><li>Integer lobortis</li><li>Curabitur ac</li><li>Phasellus tellus nisl</li><li>Aenean fringilla</li><li>Vestibulum</li><li>Aliquam commodo</li></ul>
  </div>
  <div class="rule" style="left:917px"></div>
  <div class="col" style="left:966px"><h5>Quick Links</h5>
    <ul style="left:8px"><li>Integer lobortis</li><li>Curabitur ac</li><li>Phasellus tellus nisl</li><li>Aenean fringilla</li><li>Vestibulum</li><li>Aliquam commodo</li></ul>
  </div>
</section>

<footer class="site-footer">
  <nav class="foot-nav"><a href="#">Home</a><a href="#">About us</a><a href="#">Services</a><a href="#">Products</a><a href="#">Blog</a><a href="#">Login</a><a href="#">Help</a></nav>
  <div class="foot-rule"></div>
  <p class="copyright">Copyright © 2014 &nbsp;Velmo- All rights reserved.</p>
  <div class="foot-dots"><i style="background:#3b5a98"></i><i style="background:#2fa9e0"></i><i style="background:#cd201f"></i><i style="background:#5aa13e"></i></div>
</footer>

</body>
</html>
```